Business card design needed

After a business card which portrays the same precision tig welding and performance fabrications we offer customers. Catering mainly for the automotive market, but process work for marine, industrial & hospitality work is definitely welcome.

We provide the same level quality, care and workmanship regardless of how big or small the job is. Quality is the first and foremost for customers looking for the highest standards around along with a customised look not found anywhere else.

Our offering is tailor made for each customer and where needed, a completely individual look

Colours - red, black and white (as per the attached logo)

The design should portray a customised/one-off solution for each customer with a high attention to detail.
Updates

The brief should have included this design is required for a 2 sided card

Industry/Entity Type

Hospitality

Contact Information for Business Card

Blue Anchor Metalworks
3/14 Corwen Hale Avenue
North Wollongong NSW 2500

Ph: 02 4871 3064
Mob: 0412 586 137
Email: blueanchormetalworks@mailhaven.example
Facebook: www.socialpage.example/blueanchormetalworks

Requirements
Must have
• Must have a catchy front side without being cluttered & brief but list off main offerings on the back. For eg
- customised concept & design for each project
- 2D & 3D modelling & machining
- catering for single or mass prodcued items

```html
<!DOCTYPE html>
<html lang="en">
<head>
<meta charset="utf-8">
<title>Blue Anchor Metalworks – Business Cards</title>
<link rel="stylesheet" href="https://fonts.googleapis.com/css2?family=Rubik:wght@400;500;700&display=swap">
<style>
  :root {
    --brand-red: #9b1b2a;
    --brand-red-deep: #7e1420;
    --ink: #1a1a1a;
    --card-black: #121212;
    --card-white: #fbfbfb;
    --text-grey: #2b2b2b;
    --rule: #3a3a3a;
    --page-bg: #e6e3df;
    --faint-red: #f3e4e6;
  }
  * { box-sizing: border-box; margin: 0; padding: 0; }
  html, body { width: 1200px; height: 880px; overflow: hidden; }
  body {
    background: var(--page-bg);
    font-family: "Rubik", Arial, sans-serif;
    display: flex;
    align-items: center;
    justify-content: center;
    gap: 40px;
  }
  .card {
    position: relative;
    width: 560px;
    height: 320px;
    overflow: hidden;
    box-shadow: 0 6px 18px rgba(0,0,0,0.18);
  }
  .motif { position: absolute; left: 0; top: 0; width: 560px; height: 320px; }

  /* Back side */
  .card-back { background: var(--card-black); color: #fff; }
  .card-back .wordmark {
    position: absolute;
    right: 26px; top: 44px;
    font-weight: 700;
    font-size: 20px;
    color: #fff;
  }
  .services {
    position: absolute;
    left: 312px; top: 150px;
    width: 230px;
    list-style: none;
    font-size: 12px;
    line-height: 1.45;
    color: #fff;
  }
  .services li { position: relative; padding-left: 11px; margin-bottom: 5px; }
  .services li::before {
    content: "";
    position: absolute; left: 0; top: 6px;
    width: 5px; height: 5px; border-radius: 50%;
    background: #fff;
  }

  /* Front side */
  .card-front { background: var(--card-white); color: var(--text-grey); }
  .card-front .wordmark {
    position: absolute;
    right: 26px; top: 44px;
    font-weight: 700;
    font-size: 20px;
    color: var(--ink);
  }
  .company-name {
    position: absolute;
    left: 180px; top: 116px;
    font-weight: 700;
    font-size: 19px;
    color: var(--brand-red);
  }
  .address {
    position: absolute;
    left: 180px; top: 144px;
    font-size: 12.5px;
  }
  .divider {
    position: absolute;
    left: 28px; right: 28px; top: 174px;
    border-top: 1px solid var(--rule);
  }
  .contact-list {
    position: absolute;
    list-style: none;
    font-size: 12.5px;
  }
  .contact-list li { display: flex; align-items: center; gap: 8px; margin-bottom: 10px; }
  .contact-phones { left: 28px; top: 194px; }
  .contact-online { left: 180px; top: 194px; }
  .icon { width: 14px; height: 14px; flex: none; }
</style>
</head>
<body>

  <section class="card card-back" aria-label="Business card back">
    <svg class="motif" viewBox="0 0 560 320" aria-hidden="true">
      <defs>
        <linearGradient id="panelRed" x1="0" y1="0" x2="1" y2="1">
          <stop offset="0" stop-color="var(--brand-red)"/>
          <stop offset="1" stop-color="var(--brand-red-deep)"/>
        </linearGradient>
      </defs>
      <polygon points="0,10 250,10 244,26 0,26" fill="var(--brand-red)"/>
      <polygon points="0,36 232,36 226,52 0,52" fill="var(--brand-red)"/>
      <polygon points="0,62 214,62 208,78 0,78" fill="var(--brand-red)"/>
    </svg>
    <svg class="motif" viewBox="0 0 560 320" role="img" aria-label="Bold red brand decoration">
      <polygon points="30,92 300,92 240,320 0,320 0,200" fill="url(#panelRed)"/>
    </svg>
    <div class="wordmark">Blue Anchor Metalworks</div>
    <ul class="services">
      <li>precision tig welding of all materials</li>
      <li>customised concept &amp; design for each project</li>
      <li>2D &amp; 3D modelling and machining</li>
      <li>catering for one-off &amp; production work</li>
      <li>fully equipped fabrication workshop</li>
    </ul>
  </section>

  <section class="card card-front" aria-label="Business card front">
    <svg class="motif" viewBox="0 0 560 320" aria-hidden="true">
      <polygon points="120,8 330,8 326,20 120,20" fill="var(--faint-red)"/>
      <polygon points="120,28 312,28 308,40 120,40" fill="var(--faint-red)"/>
    </svg>
    <svg class="motif" viewBox="0 0 560 320" role="img" aria-label="Faint brand decoration">
      <polygon points="150,50 340,50 290,240 90,240 120,150" fill="var(--faint-red)" opacity="0.75"/>
    </svg>
    <div class="wordmark">Blue Anchor Metalworks</div>
    <h1 class="company-name">Blue Anchor Metalworks</h1>
    <p class="address">3/14 Corwen Hale Avenue North Wollongong NSW 2500</p>
    <div class="divider"></div>

    <ul class="contact-list contact-phones">
      <li>
        <svg class="icon" viewBox="0 0 14 14" aria-hidden="true">
          <rect width="14" height="14" rx="2" fill="var(--brand-red)"/>
          <path d="M4 3.5c0 4 2.5 6.5 6.5 7l1-1.6-2-1-1 .8c-1-.5-1.8-1.3-2.2-2.2l.8-1-1-2z" fill="#fff"/>
        </svg>
        02 4871 3064
      </li>
      <li>
        <svg class="icon" viewBox="0 0 14 14" aria-hidden="true">
          <rect width="14" height="14" rx="2" fill="var(--brand-red)"/>
          <rect x="4.5" y="2.5" width="5" height="9" rx="1" fill="#fff"/>
          <rect x="5.5" y="3.7" width="3" height="5.5" fill="var(--brand-red)"/>
        </svg>
        0412 586 137
      </li>
    </ul>

    <ul class="contact-list contact-online">
      <li>
        <svg class="icon" viewBox="0 0 14 14" aria-hidden="true">
          <rect width="14" height="14" rx="2" fill="var(--brand-red)"/>
          <rect x="2.5" y="4" width="9" height="6" fill="#fff"/>
          <path d="M2.5 4l4.5 3.5L11.5 4" stroke="var(--brand-red)" stroke-width="1" fill="none"/>
        </svg>
        blueanchormetalworks@mailhaven.example
      </li>
      <li>
        <svg class="icon" viewBox="0 0 14 14" aria-hidden="true">
          <rect width="14" height="14" rx="2" fill="var(--brand-red)"/>
        </svg>
        www.socialpage.example/blueanchormetalworks
      </li>
    </ul>
  </section>

</body>
</html>
```